Flyer-Design für Physiotherapie-Praxis
Zielgruppe
Wir sind eine Praxis für Physiotherapie und möchten durch diesen Flyer neue Patienten werben. Der Flyer soll in Arztpraxen ausliegen und dort den Patienten direkt ansprechen und auf uns aufmerksam machen. Es ist auch eine Verknüpfung der Therapie mit einem Training in einem Gesundheitsstudio möglich, da im gleichen Haus das Physio Kraftwerk Eichenstetten beheimatet ist.
Aufgabenstellung
Der Fokus auf unsere Prinzipien (Ganzheitliche Therapie, hohes Maß an Therapiemöglichkeiten, Variation in den therapeutischen Ansätzen durch unterschiedlich fortgebildete Therapeuten, die nach den gleichen Idealen arbeiten)

```html
<!DOCTYPE html>
<html lang="de">
<head>
<meta charset="utf-8">
<title>Flyer Physiotherapie – Zentrum für Therapie und Training</title>
<link rel="stylesheet" href="https://fonts.googleapis.com/css2?family=Lexend:wght@300;400;500;600&display=swap">
<style>
  :root {
    --stage: #1d5168;
    --brand-blue: #0b8cc7;
    --headline-blue: #1180c2;
    --label-navy: #2b2d6b;
    --paper: #ffffff;
    --text-grey: #7a7a7a;
    --label-grey: #6f6f6f;
  }
  * { margin: 0; padding: 0; box-sizing: border-box; }
  html, body { width: 1200px; height: 1000px; overflow: hidden; }
  body {
    background: var(--stage);
    font-family: "Lexend", sans-serif;
    font-weight: 300;
    position: relative;
  }
  .flyer-side {
    position: absolute;
    left: 274px;
    width: 652px;
    height: 465px;
    display: flex;
  }
  .flyer-side--outer { top: 17px; }
  .flyer-side--inner { top: 508px; }
  .panel {
    position: relative;
    width: 217.33px;
    height: 100%;
    overflow: hidden;
  }
  .panel--blue { background: var(--brand-blue); color: var(--paper); }
  .panel--white { background: var(--paper); color: var(--text-grey); }
  .block { position: absolute; left: 16px; right: 10px; }
  .panel-title {
    font-weight: 500;
    font-size: 16px;
    line-height: 21.6px;
    letter-spacing: 0.03em;
    text-transform: uppercase;
  }
  .panel--white .panel-title { color: var(--headline-blue); }
  .body-copy { font-size: 8.3px; line-height: 12.1px; }
  .copy-stack > .body-copy + .body-copy { margin-top: 12.1px; }
  .body-copy strong { font-weight: 600; }
  .label {
    font-weight: 500;
    font-size: 9.2px;
    letter-spacing: 0.05em;
    text-transform: uppercase;
  }
  .panel--white .label { color: var(--label-grey); }
  .panel--blue .label { color: var(--label-navy); }
  .photo { position: absolute; overflow: hidden; }
  .photo--pool {
    left: 40px; top: 293px; width: 216px; height: 216px;
    border-radius: 50%;
    background: linear-gradient(180deg, #eef2f1 0%, #b9d2c4 40%, #5aa6c2 72%, #2a7fa6 100%);
  }
  .photo--massage { left: 0; top: 0; width: 100%; height: 204px; }
  .photo--team {
    left: 0; top: 173px; width: 209px; height: 136px;
    background: linear-gradient(180deg, #c9b28e 0%, #9fc7e3 45%, #86b6d8 100%);
    border-radius: 0 4px 4px 0;
  }
  .photo--gym {
    left: 0; top: 269px; width: 196px; height: 196px;
    border-radius: 50%;
    background: linear-gradient(180deg, #f3f1ec 0%, #ddd9d2 45%, #9c9893 80%, #6c6a67 100%);
  }
  .caption {
    position: absolute; left: 16px; top: 312px;
    font-size: 6.2px; font-style: italic; font-weight: 400;
  }
  .claim {
    font-size: 12.5px; line-height: 15px;
    text-transform: uppercase; font-weight: 300;
  }
  .claim strong { font-weight: 600; }
  .brand-mark {
    position: absolute; left: 0; right: 0;
    display: flex; flex-direction: column; align-items: center; gap: 6px;
  }
  .brand-mark__dot {
    width: 30px; height: 30px; border-radius: 50%;
    border: 1.2px solid currentColor;
  }
  .brand-mark__name { font-size: 9.5px; font-weight: 400; }
  .panel--white .brand-mark { color: #333; }
  .hours { display: grid; grid-template-columns: 40px auto; font-size: 8.3px; line-height: 12.1px; }
</style>
</head>
<body>

<section class="flyer-side flyer-side--outer">
  <article class="panel panel--blue">
    <h2 class="block panel-title" style="top:36px;">Vielzahl von Therapiemöglich-keiten</h2>
    <div class="block copy-stack" style="top:124px;">
      <p class="body-copy">Wir haben eine <strong>Vielzahl von Therapiegeräten</strong> und Hilfsmitteln zur Verfügung, z.B. eine Kletter-wand, Schlingentrainer, eine Vibrello®-Rüttelplatte, einen Balancesteg und ein <strong>Bewegungsbad</strong>!</p>
      <p class="body-copy">Im 32°C warmen Wasser können sich unsere Patienten besser bewegen. Mit unserem Fach-wissen und unserer Erfahrung haben wir uns auf die Behandlung orthopädischer, chirurgischer und neurologischer Patienten spezialisiert.</p>
    </div>
    <div class="photo photo--pool" role="img" aria-label="Foto des hellen Bewegungsbads mit Handlauf und Pflanzen am Fenster"></div>
  </article>

  <article class="panel panel--white">
    <h2 class="block panel-title" style="top:36px;">Kontakt</h2>
    <p class="block label" style="top:87px;">Anfahrt</p>
    <p class="block body-copy" style="top:112px;">Zentrum für Therapie und Training<br>Lorenz Albrecht &amp; Sabine Wendt</p>
    <p class="block body-copy" style="top:148px;">Lindenweg 48<br>91234 Eichenstetten</p>
    <p class="block label" style="top:184px;">Inhaber</p>
    <p class="block body-copy" style="top:208px;">Frau Sabine Wendt</p>
    <div class="brand-mark" style="top:370px;">
      <span class="brand-mark__dot"></span>
      <span class="brand-mark__name">Albrecht &amp; Wendt</span>
    </div>
  </article>

  <article class="panel panel--blue">
    <svg class="photo photo--massage" viewBox="0 0 217 204" preserveAspectRatio="none" role="img" aria-label="Foto einer Schultermassage durch Therapeutenhände">
      <defs>
        <linearGradient id="massage-tone" x1="0" y1="0" x2="1" y2="1">
          <stop offset="0" stop-color="#c9824a"/>
          <stop offset="0.5" stop-color="#a8552a"/>
          <stop offset="1" stop-color="#6e3a22"/>
        </linearGradient>
      </defs>
      <path d="M0 0 H217 V190 Q200 186 150 187 Q60 190 0 203 Z" fill="url(#massage-tone)"/>
    </svg>
    <h2 class="block claim" style="top:206px; left:18px;">Wir sind Therapeuten<br>aus <strong>Überzeugung</strong>!</h2>
    <div class="block copy-stack" style="top:247px; left:18px; right:8px;">
      <p class="body-copy" style="line-height:11px;">Unsere Praxis gibt es <strong>seit 1969</strong>. In dieser Zeit konnten wir viel Erfahrung sammeln.</p>
      <p class="body-copy" style="line-height:11px; margin-top:11px;"><strong>Wir</strong> sind ein Team aus älteren und jüngeren Therapeuten, aus Masseuren, med. Bade-meistern und Physiotherapeuten. Diese bunte Mischung beinhaltet viel <strong>Erfahrung</strong> und viel <strong>Wissen</strong>. Beides wird in regelmäßigen internen Fortbildungen ausgetauscht. So ergänzen wir uns stets gegenseitig.</p>
    </div>
    <div class="brand-mark" style="top:372px;">
      <span class="brand-mark__dot"></span>
      <span class="brand-mark__name">Albrecht &amp; Wendt</span>
    </div>
  </article>
</section>

<section class="flyer-side flyer-side--inner">
  <article class="panel panel--blue">
    <h2 class="block panel-title" style="top:35px;">Aktives Gesund-<br>heitstraining</h2>
    <p class="block body-copy" style="top:92px;">Für gute Fortschritte in der Therapie und die Er-haltung dieser Fortschritte ist der Weg zur sportlichen Aktivität essentiell. Diesen Weg erleichtern wir unseren Patienten durch unser Angebot des Aktiven Gesundheitstrainings.</p>
    <div class="photo photo--team" role="img" aria-label="Gruppenfoto des Praxisteams in hellblauen Poloshirts"></div>
    <p class="caption">Unser erfahrenes Team steht Ihnen immer zur Seite.</p>
    <p class="block body-copy" style="top:336px;">Zusätzlich zu Ihrem Rezept erhalten unsere neuen Patienten einen zusätzlichen und kosten-freien Beratungstermin im Physio Kraftwerk Eichenstetten. In diesem Termin zeigen wir Ihnen Möglichkeiten, selbst etwas zu Ihrer Gesundung beizutragen.</p>
  </article>

  <article class="panel panel--white">
    <h2 class="block panel-title" style="top:35px; left:21px;">Zirkeltraining</h2>
    <div class="block copy-stack" style="top:92px; left:21px; right:8px;">
      <p class="body-copy">Je nachdem, was Ihnen gerade am effektivsten hilft, trainieren Sie 6 x am Kraft-Ausdauer-Zirkel der Firma Vantora oder am Flexaro-Zirkel.</p>
      <p class="body-copy">Das Training an diesen Geräten ist einfach, sicher und effektiv. Da das Training maximal 35 Minuten Zeit beansprucht ist Zeitmangel kein Argument mehr. Wir arbeiten als Team Hand in Hand und schätzen das Fachwissen jedes einzelnen Kollegen.</p>
      <p class="body-copy">Wir sind motiviert und mit Freude bei der Arbeit, denn wir wissen, was unsere Patienten mit Hilfe der Physiotherapie erreichen können.</p>
    </div>
    <div class="photo photo--gym" role="img" aria-label="Foto des hellen Trainingsraums mit Kraftgeräten des Zirkels"></div>
  </article>

  <article class="panel panel--blue">
    <h2 class="block panel-title" style="top:35px; left:21px;">So erreichen<br>Sie uns!</h2>
    <p class="block label" style="top:91px; left:21px;">Online</p>
    <p class="block body-copy" style="top:108px; left:21px; right:4px;">Weitere Informationen finden Sie auf unserem Internetauftritt unter <strong>www.praxis-albrecht.de</strong>.</p>
    <p class="block label" style="top:152px; left:21px;">Telefon, Fax &amp; E-Mail</p>
    <div class="block copy-stack" style="top:169px; left:21px; right:4px;">
      <p class="body-copy">Telefonisch erreichen Sie uns unter folgender Rufnummer: <strong>0912 - 448120</strong></p>
      <p class="body-copy">Unser Telefax steht unter der Faxnummer<br><strong>0912 - 4481299</strong> für Sie bereit.</p>
      <p class="body-copy">Möchten Sie uns per E-Mail kontaktieren, dann schreiben Sie doch gerne an unsere Adresse <strong>anmeldung@praxis-albrecht.de</strong>.</p>
    </div>
    <p class="block label" style="top:298px; left:21px;">Öffnungszeiten</p>
    <p class="block body-copy" style="top:315px; left:21px;">Wir sind werktags für Sie da:</p>
    <div class="block hours" style="top:339px; left:21px;">
      <span>Mo. – Do.</span><span>07:00 – 20:00 Uhr</span>
      <span>Fr.</span><span>07:30 – 19:00 Uhr</span>
      <span>Sa.</span><span>07:30 – 12:00 Uhr</span>
    </div>
  </article>
</section>

</body>
</html>
```